Medical Device - Case Study Template

We need a TEMPLATE that we can reuse to write various case studies about the medical equipment solutions we provide. It will be a double sided letter sized with a modern design that conveys a feeling of expertise, innovation and highly personable service AND be consistent with the brand guide. The content will be divided into a few sections:

- Situation (200-250 words)
- Challenge (100-120 words)
- Solution (100-120 words)
- Results (100-120 words)
- Conclusion (100-120 words)

Additionally, there will need to be a call to action, inviting people to send an email for more information and a short "About Valtu" section (approx. 40 words).

For device picture placeholders, feel free to use any random small benchtop medical device.

```html
<!DOCTYPE html>
<html lang="en">
<head>
<meta charset="utf-8">
<title>Valtu – Medical Device Case Study Template</title>
<link rel="stylesheet" href="https://fonts.googleapis.com/css2?family=Oswald:wght@400;500;600&family=Lato:wght@400;700&display=swap">
<style>
:root{
  --backdrop:#515151;
  --paper:#ffffff;
  --orange:#f0842f;
  --orange-deep:#d0622a;
  --steel:#7aa0bd;
  --steel-text:#5f88aa;
  --ink:#1d1d1d;
  --white:#ffffff;
}
*{box-sizing:border-box;margin:0;padding:0}
html,body{width:1200px;height:1200px;overflow:hidden;background:var(--backdrop)}
body{position:relative;font-family:"Lato",sans-serif;color:var(--ink)}
.page{position:absolute;background:var(--paper);box-shadow:0 6px 18px rgba(0,0,0,.45);overflow:hidden}
.page-front{left:33px;top:67px;width:548px;height:704px}
.page-back{left:623px;top:353px;width:553px;height:710px}
.abs{position:absolute}
.heading{font-family:"Oswald",sans-serif;font-weight:500;line-height:1;display:flex;align-items:center;gap:10px;letter-spacing:-.2px}
.heading::after{content:"";flex:1;height:3px;background:currentColor}
.heading-orange{color:var(--orange)}
.heading-white{color:var(--white)}
.copy{font-size:10.2px;line-height:12.4px}
.copy-small{font-size:9.3px;line-height:11.5px}
.light{color:var(--white)}
.gradient-orange{background:linear-gradient(90deg,var(--orange),var(--orange-deep))}
/* brand */
.brand{left:30px;top:30px;display:flex;align-items:center;gap:10px}
.brand-dot{width:40px;height:40px;border-radius:50%;background:var(--orange)}
.brand-name{font-family:"Lato",sans-serif;font-weight:400;font-size:40px;color:var(--steel-text);line-height:1;letter-spacing:1px}
.brand-tag{left:109px;top:72px;font-family:"Lato",sans-serif;font-size:12.5px;color:var(--steel-text);letter-spacing:.8px}
/* front */
.hero{left:0;top:117px;width:274px;height:252px}
.hero-title{left:20px;top:36px;font-family:"Oswald",sans-serif;font-weight:600;color:var(--white);line-height:.98;white-space:nowrap}
.hero-title .line1{display:block;font-size:35px}
.hero-title .line2{display:block;font-size:26.5px}
.hero-rule{left:22px;top:103px;width:112px;height:4px;background:var(--white)}
.hero-copy{left:29px;width:232px}
.challenge-col{left:301px;top:0;width:247px;height:413px;background:var(--steel)}
.challenge-copy{left:14px;width:222px}
.photo-frame{left:301px;top:413px;width:247px;height:291px;background:var(--orange)}
.photo{left:302px;top:414px;width:231px;height:275px;background:linear-gradient(145deg,#c9ced3,#e9ecef 45%,#b7c0c8)}
.situation-copy{left:23px;width:242px}
/* back */
.solution-copy{left:16px;width:262px}
.scan-frame{left:307px;top:0;width:246px;height:253px;background:var(--orange)}
.scan-photo{left:307px;top:16px;width:229px;height:238px;background:linear-gradient(160deg,#eef1f4,#d7dde3 55%,#f4f6f8)}
.results{left:15px;top:334px;width:236px;height:360px;background:var(--steel)}
.results-copy{left:11px;width:220px}
.conclusion-copy{left:307px;width:224px}
.contacts{left:307px;top:568px;width:229px;height:126px;padding:4px 12px 0 12px}
.contact-list{list-style:none;margin:14px 0 0 24px}
.contact-list li{display:flex;align-items:flex-start;gap:10px;font-size:8.6px;line-height:10.5px;color:var(--white);margin-bottom:2.5px}
.contact-list svg{flex:none;width:9px;height:9px;margin-top:1px}
</style>
</head>
<body>

<section class="page page-front">
  <div class="abs brand"><span class="brand-dot"></span><span class="brand-name">Valtu</span></div>
  <div class="abs brand-tag">Medical Technology</div>

  <div class="abs hero gradient-orange">
    <h1 class="abs hero-title"><span class="line1">Medical Device</span><span class="line2">Case Study Template</span></h1>
    <div class="abs hero-rule"></div>
    <p class="abs hero-copy copy light" style="top:130px">Lorem ipsum dolor sit amet, consectetur adipiscing elit, sed do eiusmod tempor incididunt ut labore et dolore magna aliqua. Ut enim ad minim veniam, quis nostrud exercitation ullamco laboris nisi ut aliquip ex ea commodo consequat.</p>
    <p class="abs hero-copy copy light" style="top:200px">Lorem ipsum dolor sit amet, consectetur adipiscing elit, sed do eiusmod tempor incididunt ut .</p>
  </div>

  <h2 class="abs heading heading-orange" style="left:22px;top:391px;font-size:28px;width:218px">Situation</h2>
  <p class="abs situation-copy copy" style="top:439px">Lorem ipsum dolor sit amet, consectetur adipiscing elit, sed do eiusmod tempor incididunt ut labore et dolore magna aliqua. Ut enim ad minim veniam, quis nostrud exercitation ullamco laboris nisi ut aliquip ex ea commodo consequat. Duis aute irure dolor in reprehenderit in voluptate velit esse cillum dolore eu fugiat nulla pariatur. Excepteur sint occaecat cupidatat non proident, sunt in culpa qui officia deserunt mollit anim id est laborum.</p>
  <p class="abs situation-copy copy" style="top:562px;left:27px">Lorem ipsum dolor sit amet, consectetur adipiscing elit, sed do eiusmod tempor incididunt ut labore et dolore magna aliqua. Ut enim ad minim veniam, quis nostrud exercitation ullamco laboris nisi ut aliquip ex ea commodo consequat. Duis aute irure dolor in reprehenderit in voluptate velit esse cillum dolore eu fugiat nulla pariatur. Excepteur sint occaecat cupidatat non proident, sunt in culpa qui officia deserunt mollit anim id est laborum.</p>

  <div class="abs challenge-col">
    <h2 class="abs heading heading-white" style="left:14px;top:26px;font-size:28px;width:207px">Challenge</h2>
    <p class="abs challenge-copy copy light" style="top:65px">Lorem ipsum dolor sit amet, consectetur adipiscing elit, sed do eiusmod tempor incididunt ut labore et dolore magna aliqua. Ut enim ad minim veniam, quis nostrud exercitation ullamco laboris nisi ut aliquip ex ea commodo consequat. Duis aute irure dolor in reprehenderit in voluptate velit esse cillum dolore eu fugiat nulla pariatur. Excepteur sint occaecat cupidatat non proident, sunt in culpa qui officia deserunt mollit anim id est laborum.</p>
    <p class="abs challenge-copy copy light" style="top:198px">Lorem ipsum dolor sit amet, consectetur adipiscing elit, sed do eiusmod tempor incididunt ut labore et dolore magna aliqua. Ut enim ad minim veniam, quis nostrud exercitation ullamco laboris nisi ut aliquip ex ea commodo consequat. Duis aute irure dolor in reprehenderit in voluptate velit esse cillum dolore eu fugiat nulla pariatur. Excepteur sint occaecat cupidatat non proident, sunt in culpa qui officia deserunt mollit anim id est laborum.</p>
    <p class="abs challenge-copy copy light" style="top:339px">Lorem ipsum dolor sit amet, consectetur adipiscing elit, sed do eiusmod tempor incididunt ut labore et dolore magna aliqua. Ut enim ad minim veniam, quis nostrud exercitation ullamco laboris nisi ut aliquip ex ea commodo consequat.</p>
  </div>
  <div class="abs photo-frame"></div>
  <div class="abs photo" role="img" aria-label="Photo of patient monitors and a ventilator in a clinical room"></div>
</section>

<section class="page page-back">
  <h2 class="abs heading heading-orange" style="left:16px;top:24px;font-size:33px;width:248px">Solution</h2>
  <p class="abs solution-copy copy-small" style="top:82px">Lorem ipsum dolor sit amet, consectetur adipiscing elit, sed do eiusmod tempor incididunt ut labore et dolore magna aliqua. Ut enim ad minim veniam, quis nostrud exercitation ullamco laboris nisi ut aliquip ex ea commodo consequat. Duis aute irure dolor in reprehenderit in voluptate velit esse cillum dolore eu fugiat nulla pariatur. Excepteur sint occaecat cupidatat non proident, sunt in culpa qui officia deserunt mollit anim id est laborum.</p>
  <p class="abs solution-copy copy-small" style="top:184px">Lorem ipsum dolor sit amet, consectetur adipiscing elit, sed do eiusmod tempor incididunt ut labore et dolore magna aliqua. Ut enim ad minim veniam, quis nostrud exercitation ullamco laboris nisi ut aliquip ex ea commodo consequat. Duis aute irure dolor in reprehenderit in voluptate velit esse cillum dolore eu fugiat nulla pariatur. Excepteur sint occaecat cupidatat non proident, sunt in culpa qui officia deserunt mollit anim id est laborum.</p>
  <p class="abs solution-copy copy-small" style="top:286px">Lorem ipsum dolor sit amet, consectetur adipiscing elit, sed do eiusmod tempor incididunt ut labore et dolore magna aliqua. Ut enim ad minim veniam, quis nostrud exercitation</p>

  <div class="abs results">
    <h2 class="abs heading heading-white" style="left:10px;top:6px;font-size:33px;width:206px">Results</h2>
    <p class="abs results-copy copy-small light" style="top:53px">Lorem ipsum dolor sit amet, consectetur adipiscing elit, sed do eiusmod tempor incididunt ut labore et dolore magna aliqua. Ut enim ad minim veniam, quis nostrud exercitation ullamco laboris nisi ut aliquip ex ea commodo consequat. Duis aute irure dolor in reprehenderit in voluptate velit esse cillum dolore eu fugiat nulla pariatur. Excepteur sint occaecat cupidatat non proident, sunt in culpa qui officia deserunt mollit anim id est laborum.</p>
    <p class="abs results-copy copy-small light" style="top:167px">Lorem ipsum dolor sit amet, consectetur adipiscing elit, sed do eiusmod tempor incididunt ut labore et dolore magna aliqua. Ut enim ad minim veniam, quis nostrud exercitation ullamco laboris nisi ut aliquip ex ea commodo consequat. Duis aute irure dolor in reprehenderit in voluptate velit esse cillum dolore eu fugiat nulla pariatur. Excepteur sint occaecat cupidatat non proident, sunt in culpa qui officia deserunt mollit anim id est laborum.</p>
    <p class="abs results-copy copy-small light" style="top:281px">Lorem ipsum dolor sit amet, consectetur adipiscing elit, sed do eiusmod tempor incididunt ut labore et dolore magna aliqua. Ut enim ad minim veniam, quis nostrud exercitation .</p>
  </div>

  <div class="abs scan-frame"></div>
  <div class="abs scan-photo" role="img" aria-label="Photo of a CT scanner in a bright hospital room"></div>

  <h2 class="abs heading heading-orange" style="left:307px;top:274px;font-size:33px;width:216px">Conclusion</h2>
  <p class="abs conclusion-copy copy-small" style="top:322px">Lorem ipsum dolor sit amet, consectetur adipiscing elit, sed do eiusmod tempor incididunt ut labore et dolore magna aliqua. Ut enim ad minim veniam, quis nostrud exercitation ullamco laboris nisi ut aliquip ex ea commodo consequat. Duis aute irure dolor in reprehenderit in voluptate velit esse cillum dolore eu fugiat nulla pariatur. Excepteur sint occaecat cupidatat non proident, sunt in culpa qui officia deserunt mollit anim id est laborum.</p>
  <p class="abs conclusion-copy copy-small" style="top:436px">Lorem ipsum dolor sit amet, consectetur adipiscing elit, sed do eiusmod tempor incididunt ut labore et dolore magna aliqua. Ut enim ad minim veniam, quis nostrud exercitation ullamco laboris nisi ut aliquip ex ea commodo consequat. Duis aute irure dolor in reprehenderit in voluptate velit esse cillum dolore eu fugiat nulla pariatur. Excepteur sint occaecat cupidatat non proident, sunt in culpa qui officia deserunt mollit anim id est laborum.</p>

  <div class="abs contacts gradient-orange">
    <h2 class="heading heading-white" style="font-size:32px;gap:0;flex-direction:column;align-items:stretch">Contacts</h2>
    <ul class="contact-list">
      <li><svg viewBox="0 0 10 10"><path d="M5 0.5a3.3 3.3 0 0 0-3.3 3.3C1.7 6.3 5 9.5 5 9.5s3.3-3.2 3.3-5.7A3.3 3.3 0 0 0 5 .5zm0 4.6a1.3 1.3 0 1 1 0-2.6 1.3 1.3 0 0 1 0 2.6z" fill="#fff"/></svg><span>Lorem ipsum dolor sit amet, consectetur adipiscing elit</span></li>
      <li><svg viewBox="0 0 10 10"><circle cx="5" cy="5" r="4.3" fill="none" stroke="#fff" stroke-width=".8"/><path d="M3.4 2.8l1 .9-.5.7c.4.8.9 1.3 1.6 1.7l.7-.5.9 1-.6.7c-1.8-.4-3.3-1.9-3.7-3.8z" fill="#fff"/></svg><span>012345678900</span></li>
      <li><svg viewBox="0 0 10 10"><rect x=".7" y="2" width="8.6" height="6" fill="none" stroke="#fff" stroke-width=".9"/><path d="M.7 2L5 5.6 9.3 2" fill="none" stroke="#fff" stroke-width=".9"/></svg><span>info@companyname.com</span></li>
      <li><svg viewBox="0 0 10 10"><circle cx="5" cy="5" r="4.2" fill="none" stroke="#fff" stroke-width=".8"/><ellipse cx="5" cy="5" rx="1.8" ry="4.2" fill="none" stroke="#fff" stroke-width=".7"/><path d="M.8 5h8.4M1.5 3h7M1.5 7h7" stroke="#fff" stroke-width=".6"/></svg><span>www.companyname.com</span></li>
    </ul>
  </div>
</section>

</body>
</html>
```